Town Planning Consultants require lstationary design

Require a design to be used for our letterhead and report cover page. We have an approved logo.
we have attached our logo, and our temporary letterhead/cover page (SEE Cover) which we currently adapt for both purposes in the interim pending a permanent design. I have also attached an example (example report cover) of a report cover page that I like. perhaps similar with our colour scheme

Target Market(s)

?

Industry/Entity Type

Town

Colors
249fd4
3176b5

Requirements
Must have
• colours to match logo
• the text content in existing letterhead

```html
<!DOCTYPE html>
<html lang="en">
<head>
<meta charset="utf-8">
<title>Parkline – Stationery</title>
<link rel="stylesheet" href="https://fonts.googleapis.com/css2?family=Exo+2:wght@400;500&family=Open+Sans:wght@400;600&display=swap">
<style>
  :root {
    --brand-blue: #24a6db;
    --band-grey: #9b9b9b;
    --title-grey: #8c8c8c;
    --text-grey: #7a7a7a;
    --paper: #ffffff;
    --backdrop: #e9ebee;
  }
  * { margin: 0; padding: 0; box-sizing: border-box; }
  html, body { width: 1200px; height: 917px; overflow: hidden; }
  body {
    background: var(--backdrop);
    position: relative;
    font-family: "Open Sans", sans-serif;
  }
  .sheet {
    position: absolute;
    top: 112px;
    width: 538px;
    height: 695px;
    background: var(--paper);
    box-shadow: 4px 6px 14px rgba(0,0,0,0.25);
    overflow: hidden;
  }
  .report-cover { left: 42px; }
  .letterhead { left: 620px; }

  /* Report cover */
  .doc-type {
    position: absolute; left: 30px; top: 37px;
    width: 266px; height: 27px;
    background: var(--brand-blue);
    color: #fff;
    font-family: "Exo 2", sans-serif;
    font-size: 15px; letter-spacing: 0.3px;
    display: flex; align-items: center; justify-content: center;
  }
  .doc-title {
    position: absolute; left: 31px; top: 84px;
    font-family: "Exo 2", sans-serif; font-weight: 500;
    font-size: 24px; line-height: 26px;
    color: var(--title-grey);
  }
  .cover-brand {
    position: absolute; left: 330px; top: 92px;
    font-family: "Exo 2", sans-serif; font-weight: 400;
    font-size: 46px; line-height: 1;
    color: var(--brand-blue);
  }
  .cover-illustration {
    position: absolute; left: 0; top: 155px;
    width: 538px; height: 272px;
  }
  .council-band {
    position: absolute; left: 0; top: 427px;
    width: 100%; height: 43px;
    background: var(--band-grey);
    color: #fff;
    font-family: "Exo 2", sans-serif;
    font-size: 28px;
    display: flex; align-items: center; justify-content: center;
  }
  .cover-footer {
    position: absolute; left: 0; top: 470px;
    width: 100%; height: 225px;
    background: var(--brand-blue);
  }
  .site-ref {
    position: absolute; left: 34px; top: 29px;
    width: 474px; height: 25px;
    background: #fff; color: var(--brand-blue);
    font-size: 12px;
    display: flex; align-items: center; justify-content: center;
  }
  .proposal {
    position: absolute; left: 34px; top: 69px;
    color: #fff; font-size: 11px; letter-spacing: 0.2px;
  }
  .issue-date {
    position: absolute; left: 419px; top: 178px;
    width: 88px; height: 22px;
    border: 1px solid #fff;
    color: #fff; font-size: 9.5px;
    display: flex; align-items: center; justify-content: center;
  }
  .issue-date sup { font-size: 6px; }

  /* Letterhead */
  .letter-brand {
    position: absolute; left: 22px; top: 40px;
    font-family: "Exo 2", sans-serif;
    font-size: 32px; line-height: 1;
    color: var(--brand-blue);
  }
  .contact-list {
    position: absolute; right: 24px; top: 19px;
    list-style: none;
    font-size: 11px; line-height: 14px;
    color: var(--text-grey);
  }
  .contact-list li { display: flex; align-items: center; gap: 5px; }
  .contact-list svg { width: 8px; height: 8px; fill: none; stroke: var(--brand-blue); stroke-width: 1.6; }
  .header-rule {
    position: absolute; left: 22px; right: 24px; top: 77px;
    height: 2px; background: var(--brand-blue);
  }
  .letter-footer {
    position: absolute; left: 0; bottom: 0;
    width: 100%; height: 25px;
    background: var(--band-grey);
    color: #fff; font-size: 11px;
    display: flex; align-items: center; justify-content: center;
  }
</style>
</head>
<body>

<section class="sheet report-cover">
  <div class="doc-type">DEVELOPMENT APPLICATION</div>
  <h1 class="doc-title">Statement of<br>Environmental Effects</h1>
  <div class="cover-brand">Parkline</div>

  <svg class="cover-illustration" viewBox="0 0 538 272" role="img" aria-label="Simplified blue building blocks illustration">
    <rect x="350" y="0" width="188" height="116" fill="var(--brand-blue)"/>
    <rect x="45" y="45" width="274" height="227" fill="var(--brand-blue)"/>
    <rect x="350" y="157" width="149" height="115" fill="var(--brand-blue)"/>
  </svg>

  <div class="council-band">Northgate Shire Council</div>

  <div class="cover-footer">
    <div class="site-ref">LOT 3 DP 512840 &amp; Lot 9 DP41207 No 215 Ridgeview Road &amp; No 8 Mill Lane</div>
    <p class="proposal">Redevelopment of an Existing Shopping Centre in 2 Stages for “Shop top Housing”.</p>
    <div class="issue-date">25<sup>TH</sup>&nbsp;JULY, 2016</div>
  </div>
</section>

<section class="sheet letterhead">
  <div class="letter-brand">Parkline</div>
  <ul class="contact-list">
    <li><svg viewBox="0 0 10 10"><path d="M2 1 L4 3 L3 4 Q4 6 6 7 L7 6 L9 8 L8 9 Q3 9 1 2 Z"/></svg>+330 5550-1234</li>
    <li><svg viewBox="0 0 10 10"><rect x="1" y="4" width="8" height="4"/><rect x="3" y="1" width="4" height="3"/></svg>+330 5550-5678</li>
    <li><svg viewBox="0 0 10 10"><rect x="1" y="2" width="8" height="6"/><path d="M1 2 L5 6 L9 2"/></svg>info@parkline.com</li>
    <li><svg viewBox="0 0 10 10"><circle cx="5" cy="5" r="4"/><path d="M1 5 H9 M5 1 Q2 5 5 9 M5 1 Q8 5 5 9"/></svg>www.parkline.com</li>
  </ul>
  <div class="header-rule"></div>
  <footer class="letter-footer">42 N. Harbor St., Lakeview, WA 99010</footer>
</section>

</body>
</html>
```